New Church Home Page and Content Page Design

Our church, Cedar Hollow Baptist Church www.chbcfenway.example, needs an update for our online presence. The homepage design should provide the following 4 pieces of information above the fold:
1. Church location - 47 Linden Brook Lane in Chappaqua, NY, USA.
2. Service times and types Sunday school, children's church, etc..
3. A space for some text describing us and our beliefs - a Bible believing independent Baptist church.
4. photos of our members to give visitors an impression of what kind of people attend our church - a friendly group of culturally diverse people who love Jesus.

In addition to the homepage we need a design for internal pages of general content. The content page design should provide a lot of room for content and prominent navigation area. We will use this design to host pages with content such as:
A full description of our beliefs
A photo gallery
An event calendar
Embedded audio and video of past sermons
A member directory
etc.
Updates

Thanks everyone for your submissions. I'll be meeting with our Pastor tomorrow. I am working as fast as I can to review all the designs and come up with a short list for him. A decision should be close behind.

Target Market(s)

Local people looking for a church.

Industry/Entity Type

Church

Requirements
Must have
• 1. Place to show church location - Harrow Glen county, Northland State, USA.
2. Place to list service times and types.
3. A space for some text describing us and our beliefs.
4. A place to display photos of our members (see also the nice to have section)
Nice to have
• Would be great if the member photos (#4 in must have section) displayed the images in some innovative way. I rather not have an ordinary carousel of images.

```html
<!DOCTYPE html>
<html lang="en">
<head>
<meta charset="utf-8">
<title>Cedar Hollow Baptist Church</title>
<link href="https://fonts.googleapis.com/css2?family=Montserrat:wght@400;500&family=Noto+Serif:wght@400;700&family=Arimo:wght@400;700&display=swap" rel="stylesheet">
<style>
:root{
  --navy:#1b3a5f;
  --navy-dark:#132a46;
  --ink:#1a1a1a;
  --text:#555a60;
  --muted:#8a8f95;
  --white:#ffffff;
  --band:#eeeff0;
  --line:#c9c9c9;
  --link:#3f6aa1;
}
*{box-sizing:border-box;margin:0;padding:0}
html,body{width:1200px;height:1100px;overflow:hidden;background:var(--white)}
body{position:relative;font-family:"Noto Serif",serif;color:var(--ink)}
.abs{position:absolute}

.topbar{left:0;top:0;width:1200px;height:28px;background:var(--navy)}
.social{left:233px;top:0;display:flex}
.social span{width:38px;height:28px;border-right:1px solid #2d4b70;border-left:1px solid #2d4b70;display:flex;align-items:center;justify-content:center}
.social span i{width:12px;height:12px;background:#5a7190;display:block}
.region{right:236px;top:6px;color:var(--white);font:500 13px "Montserrat",sans-serif;letter-spacing:.5px}

.brand{left:232px;top:42px;display:flex;align-items:center;gap:8px}
.brand .mark{width:40px;height:34px;background:var(--navy)}
.brand .name{font:500 11.5px/13px "Montserrat",sans-serif;color:var(--navy);width:82px}
.nav{left:0;top:56px;width:1200px;height:18px;font:400 12.5px "Montserrat",sans-serif;color:var(--navy)}
.nav a{position:absolute;top:0;color:inherit;text-decoration:none;letter-spacing:.4px}
.nav a.active{color:#9aa0a8}

.hero{left:0;top:90px;width:1200px;height:205px;background:linear-gradient(180deg,#cdbba3 0%,#a98a6a 45%,#6f5136 100%)}
.hero-dots{left:912px;top:100px;display:flex;gap:3px}
.hero-dots i{width:5px;height:5px;border-radius:50%;background:#d8d8d8;display:block}
.hero-dots i.on{background:#c9302c}
.mission{left:228px;top:240px;width:737px;height:51px;background:rgba(40,34,30,.55);color:var(--white);font:400 17.5px/23px "Montserrat",sans-serif;padding:6px 4px;letter-spacing:.8px}

.band{left:0;top:295px;width:1200px;height:96px;background:var(--navy)}
.countdown{left:223px;top:314px;width:359px;height:35px;background:var(--navy-dark);border:1px solid #2f4c70;color:var(--white);font-family:"Arimo",sans-serif;display:flex;align-items:center;padding-left:20px}
.countdown .next{font-size:7.5px;line-height:11px;color:#c8d0da;width:84px}
.countdown .next b{font-weight:400;color:var(--white);font-size:8px}
.countdown .unit{margin-right:10px;font-size:8px}
.countdown .unit b{font-size:13px;letter-spacing:1.5px;margin-right:3px}
.download{left:697px;top:320px;width:270px;height:29px;background:var(--navy-dark);border:1px solid #8494a8;color:var(--white);font:400 13px/27px "Montserrat",sans-serif;text-align:center;letter-spacing:.6px}

.panel{left:230px;top:373px;width:735px;height:409px;background:var(--white);box-shadow:0 2px 6px rgba(0,0,0,.25);border-bottom:7px solid #3a3d42}
.card{position:absolute;width:209px;text-align:center}
.card .photo{height:109px;border:3px solid #f3f3f3;box-shadow:0 1px 3px rgba(0,0,0,.35);display:flex;align-items:center;justify-content:center;font:400 36px "Noto Serif",serif;color:var(--white);letter-spacing:1px;text-shadow:0 1px 3px rgba(0,0,0,.4)}
.card h3{font:400 14px "Noto Serif",serif;letter-spacing:1.2px;color:var(--navy);margin-top:8px;line-height:14px}
.card p{font-size:8.5px;line-height:10px;letter-spacing:.3px;margin-top:1px}
.card .more{font-size:8.5px;margin-top:9px;letter-spacing:.3px}
.hope{background:linear-gradient(180deg,#2c4a72,#8aa4c2 60%,#e7eef4)}
.believe{background:linear-gradient(180deg,#b66f86,#8a3f58 55%,#3e2a44)}
.values{background:linear-gradient(180deg,#5a8f94,#a9ccc9 60%,#e9f0e6)}

.section-bar{position:absolute;height:21px;background:var(--navy);color:var(--white);font:400 14px/21px "Noto Serif",serif;letter-spacing:1px;padding-left:14px}
.prayer-photo{left:25px;top:233px;width:207px;height:159px;background:radial-gradient(ellipse at 50% 55%,#b3a48c,#6b5d4c 70%,#3f362e);border:2px solid #eee;box-shadow:0 1px 3px rgba(0,0,0,.3)}
.beliefs{left:249px;top:242px;width:200px;list-style:none;font-size:11px;line-height:12.5px;letter-spacing:.3px}
.beliefs li{margin-bottom:29px}
.beliefs li::before{content:"▪ ";font-size:9px}
.events{left:496px;top:236px;width:140px;list-style:none;font-size:11px;line-height:12.5px;letter-spacing:.7px}
.events li{padding-bottom:4px;border-bottom:1px solid var(--line);margin-bottom:7px}
.events li:last-child{border:none}

.sermons{left:0;top:776px;width:1200px;height:161px;background:var(--band)}
.sermon{position:absolute;top:26px;width:223px;font-family:"Arimo",sans-serif}
.sermon h4{font:700 9.5px "Arimo",sans-serif;letter-spacing:1.5px;color:#2a2a2a}
.player{margin-top:3px;height:18px;background:#2f3338;border-radius:2px;display:flex;align-items:center;color:#ddd;font-size:7.5px;padding:0 8px}
.player .play{width:0;height:0;border-left:6px solid #ddd;border-top:4px solid transparent;border-bottom:4px solid transparent;margin-right:19px}
.player .bar{width:40px;height:3px;background:#4a86c5;margin-left:auto;margin-right:16px}
.player .vol{width:8px;height:7px;background:#ddd}
.sermon p{margin-top:5px;font-size:8.2px;line-height:12.6px;color:var(--muted);letter-spacing:.6px}
.sermon .ref{color:#222;font-weight:700;margin-top:3px;font-size:8.5px;letter-spacing:.5px}
.sermon .more{font-style:italic;color:var(--link);font-size:8.5px;margin-top:5px}

.members{left:0;top:947px;width:1200px;height:115px;background:var(--navy)}
.member{position:absolute;top:25px;width:158px;height:66px;border:1px solid #d6d6d6;box-shadow:0 1px 3px rgba(0,0,0,.4)}
.arrow{position:absolute;top:43px}
.powered{left:842px;top:1072px;font-size:10.5px;letter-spacing:.6px}
</style>
</head>
<body>

<div class="abs topbar"></div>
<div class="abs social"><span><i></i></span><span><i></i></span><span><i></i></span></div>
<div class="abs region">Harrow Glen county, Northland State, USA.</div>

<div class="abs brand"><div class="mark"></div><div class="name">Cedar Hollow Baptist Church</div></div>
<nav class="abs nav">
  <a class="active" href="#" style="left:432px">Home</a>
  <a href="#" style="left:493px">Sermons</a>
  <a href="#" style="left:579px">News</a>
  <a href="#" style="left:643px">Gallery</a>
  <a href="#" style="left:718px">Events</a>
  <a href="#" style="left:783px">Locations</a>
  <a href="#" style="left:867px">Staff</a>
  <a href="#" style="left:918px">Contact</a>
</nav>

<div class="abs hero" role="img" aria-label="Blurred church sanctuary interior with pews"></div>
<div class="abs hero-dots"><i></i><i class="on"></i><i></i><i></i><i></i></div>
<div class="abs mission">Our mission is to guide people of all<br>backgrounds into a personal relationship with Jesus Christ.</div>

<div class="abs band"></div>
<div class="abs countdown">
  <div class="next">Upcoming:<br><b>All Day Prayer</b></div>
  <span class="unit"><b>25</b>days</span>
  <span class="unit"><b>04</b>hours</span>
  <span class="unit"><b>41</b>minutes</span>
  <span class="unit"><b>32</b>seconds</span>
</div>
<div class="abs download">Download Latests Sermon</div>

<div class="abs panel">
  <div class="card" style="left:23px;top:15px">
    <div class="photo hope" role="img" aria-label="Blue cloudy sky">HOPE</div>
    <h3>SERMONS</h3>
    <p>The page content here will not be<br>displayer if you have selected this</p>
    <div class="more">Read more →</div>
  </div>
  <div class="card" style="left:266px;top:15px">
    <div class="photo believe" role="img" aria-label="Pink sunset clouds">BELIEVE</div>
    <h3>ABOUT US</h3>
    <p>This is the Excerpt of the About Page. It<br>will be used whenever you choose to dis</p>
    <div class="more">Read more →</div>
  </div>
  <div class="card" style="left:505px;top:15px">
    <div class="photo values" role="img" aria-label="Teal sky with bright clouds">VALUES</div>
    <h3>CONTACT</h3>
    <p>Nulla consequat massa quis enim.<br>Donec pede justo, fringilla vel,</p>
    <div class="more">Read more →</div>
  </div>

  <div class="section-bar" style="left:21px;top:201px;width:409px">Our Core Believes</div>
  <div class="section-bar" style="left:482px;top:202px;width:228px">Upcoming Events</div>

  <div class="abs prayer-photo" role="img" aria-label="Hands folded in prayer, sepia tone"></div>
  <ul class="abs beliefs">
    <li>We proclaim Jesus Christ and promote communities of joy.</li>
    <li>We proclaim Jesus Christ and promote communities of joy.</li>
    <li>We proclaim Jesus Christ and promote communities of joy.</li>
  </ul>
  <ul class="abs events">
    <li>All Day Prayer<br>May 17, 2014</li>
    <li>Sunday Prayers<br>June 15, 2014 8:00 am</li>
    <li style="width:170px;border-bottom:none">Sunday Prayers<br>October 12, 2014 8:00 am</li>
    <li>Pilgrimage<br>November 30, 2014</li>
  </ul>
</div>

<div class="abs sermons">
  <div class="sermon" style="left:238px">
    <h4>SERMONIUM</h4>
    <div class="player"><span class="play"></span>00:00 | 03:34<span class="bar"></span><span class="vol"></span></div>
    <p>For the love of money is the root of all evil: which while some coveted after, they have erred from the faith, and pierced themselves through with many sorrows.</p>
    <p class="ref">Bible, 1 Timothy 6:10</p>
  </div>
  <div class="sermon" style="left:489px">
    <h4>ANOTHER SERMON</h4>
    <div class="player"><span class="play"></span>00:00 | 00:00<span class="bar"></span><span class="vol"></span></div>
    <p>Lorem ipsum dolor sit amet, consectetuer adipiscing elit. Aenean commodo ligula eget dolor. Aenean massa. Cum sociis natoque penatibus et magnis dis parturient montes, nascetur ridiculus mus.</p>
    <p class="more">Read more →</p>
  </div>
  <div class="sermon" style="left:740px">
    <h4>SUNDAY SERMON</h4>
    <div class="player"><span class="play"></span>00:00 | 03:34<span class="bar"></span><span class="vol"></span></div>
    <p>Lorem ipsum dolor sit amet, consectetuer adipiscing elit. Aenean commodo ligula eget dolor. Aenean massa. Cum sociis natoque penatibus et magnis dis parturient montes, nascetur ridiculus mus.</p>
    <p class="more">Read more →</p>
  </div>
</div>

<div class="abs members">
  <svg class="arrow" style="left:180px" width="22" height="30" viewBox="0 0 22 30"><path d="M18 2 L5 15 L18 28" fill="none" stroke="#5f7899" stroke-width="4"/></svg>
  <div class="member" style="left:232px;background:linear-gradient(135deg,#7a9bb5,#d9b89a 50%,#8a6b55)" role="img" aria-label="Smiling family of four"></div>
  <div class="member" style="left:425px;background:linear-gradient(180deg,#2e6fb0,#8fb7dc 55%,#e6eef4)" role="img" aria-label="Child jumping against a blue sky"></div>
  <div class="member" style="left:617px;background:linear-gradient(135deg,#e9e2d6,#cdb8a0 50%,#e7a7b8)" role="img" aria-label="Young girls holding flower bouquets"></div>
  <div class="member" style="left:809px;background:linear-gradient(180deg,#a9abad,#d9d9d8 60%,#8e9092)" role="img" aria-label="Open Bible on a table"></div>
  <svg class="arrow" style="left:998px" width="22" height="30" viewBox="0 0 22 30"><path d="M4 2 L17 15 L4 28" fill="none" stroke="#5f7899" stroke-width="4"/></svg>
</div>

<div class="abs powered">Powered By xyz</div>

</body>
</html>
```